Family Farm Business Requires Flyer for local CSA retail sales and local advertising

We need a flyer design for our small farm to help promote our CSA business. A CSA is when someone pre-pays for a summer's worth of produce, fruit, and eggs that are raised on our farm. They receive a weekly box of produce and essentially they buy a small share of the summer's bounty. We had a logo designed by someone here on sketch harbor so we would like the flyer to include the colors of the logo. The final design should reflect the different options for people the choose and then invite them to sign up to be a CSA Customer.

Target Market(s)

Busy families and moms who are limited in time to buy groceries or healthy food or produce. People who are passionate about local food and local produce.

Industry/Entity Type

Advertising

Font styles to use
Decorative
Script

Requirements
Must have
• Our logo, our farm information (website, social media, location) and contact info as well as the various options to choose from for our CSA farm share. I also included a picture of our business card so it would be good if it matched the colors/style of our card. Also the flyer will be printed on 8.5 x 11 paper and it will be double sided.

```html
<!DOCTYPE html>
<html lang="en">
<head>
<meta charset="utf-8">
<title>Maple Hollow Farm – Summer CSA Flyer</title>
<link rel="stylesheet" href="https://fonts.googleapis.com/css2?family=Alex+Brush&family=Raleway:wght@300;400&display=swap">
<style>
  :root {
    --farm-green: #1c8a4e;
    --ink: #4a4a4a;
    --ink-soft: #6a6a6a;
    --paper: #ffffff;
    --backdrop: #e9ebe8;
  }
  * { margin: 0; padding: 0; box-sizing: border-box; }
  html, body { width: 1200px; height: 1123px; overflow: hidden; }
  body {
    background: var(--backdrop);
    font-family: "Raleway", Arial, sans-serif;
    font-weight: 300;
    color: var(--ink);
  }
  .flyer {
    position: absolute;
    left: 40px; top: 128px;
    width: 1120px; height: 868px;
    background: var(--paper);
  }
  .column { position: absolute; top: 0; }
  .column--left { left: 66px; width: 470px; }
  .column--right { left: 576px; width: 500px; }

  .script-heading {
    font-family: "Alex Brush", cursive;
    font-weight: 400;
    color: var(--farm-green);
    font-size: 34px;
    line-height: 1.05;
  }
  .options-heading { margin-top: 36px; }
  .pickup-heading { margin-top: 26px; width: 360px; }
  .payment-heading { margin-top: 24px; }

  .intro { font-size: 17px; line-height: 28px; margin-top: 6px; }

  .choice-list { list-style: none; margin-top: 8px; }
  .choice-list li {
    position: relative;
    padding-left: 49px;
    font-size: 17px;
    line-height: 28px;
  }
  .choice-list li::before {
    content: "";
    position: absolute;
    left: 2px; top: 9px;
    width: 11px; height: 11px;
    border: 1px solid var(--ink);
  }
  .payment-list { list-style: none; margin-top: 10px; }
  .payment-list li {
    position: relative;
    padding-left: 49px;
    font-size: 17px;
    line-height: 28px;
  }
  .payment-list li::before {
    content: "";
    position: absolute;
    left: 2px; top: 12px;
    width: 5px; height: 5px;
    border-radius: 50%;
    background: var(--ink);
  }

  .responsibilities {
    margin-top: 42px;
    font-size: 14px;
    line-height: 25px;
    color: var(--ink-soft);
  }
  .responsibilities .lead { font-size: 21px; color: var(--ink); }
  .responsibilities .shout { font-size: 19px; color: var(--ink); }
  .responsibilities u { text-decoration: underline; }

  .thanks {
    position: absolute;
    left: 184px; top: 450px;
    font-size: 44px;
    line-height: 54px;
  }

  .brand {
    position: absolute;
    left: 6px; top: 640px;
    width: 110px;
    display: flex; flex-direction: column; align-items: center; gap: 10px;
  }
  .brand-dot { width: 28px; height: 28px; border-radius: 50%; background: var(--farm-green); }
  .brand-name {
    color: var(--farm-green);
    font-size: 22px;
    font-weight: 400;
    line-height: 26px;
    text-align: center;
    text-transform: uppercase;
    letter-spacing: 1px;
  }

  .contact { position: absolute; left: 140px; top: 640px; list-style: none; }
  .contact li {
    display: flex; align-items: flex-start; gap: 16px;
    color: var(--farm-green);
    font-size: 20px;
    font-weight: 400;
    line-height: 28px;
    margin-bottom: 10px;
  }
  .contact svg { flex: none; width: 32px; height: 32px; }
</style>
</head>
<body>
<main class="flyer">
  <section class="column column--left">
    <h2 class="script-heading options-heading">Options: (Please Check)</h2>
    <p class="intro">Summer CSA (18 weeks – weekly delivery starting June 1st through October 11th)</p>
    <ul class="choice-list">
      <li>Mini Share (1 to 2 people) $325.00</li>
      <li>Standard Share ( 4 to 6 people) $425.00</li>
      <li>Family Share $500.00 (6 to 8 people)</li>
      <li>Fruit Share Add-on&nbsp; $50 to $75 depending on size (please indicate when ordering)</li>
      <li>Egg Share Add-on $90</li>
    </ul>

    <h2 class="script-heading pickup-heading">Preferred Pick Up Location for Summer CSA</h2>
    <ul class="choice-list">
      <li>At Maple Hollow Farm on Thursdays (1275 Orchard Lane Fernbrook, VA 24099)</li>
      <li>Fernbrook Farmers Market on Saturdays&nbsp;&nbsp; (Circle One:&nbsp; Pre-Picked Market Shopper)</li>
      <li>Stonebridge Community Church Millbrook on Thursday Afternoons</li>
    </ul>

    <h2 class="script-heading payment-heading">Payment Options</h2>
    <ul class="payment-list">
      <li>Check made payable to: Daniel Whitcomb / Maple Hollow Farm</li>
      <li>Debit/Credit Card/PayNest paid on website (coming soon!)</li>
      <li>Money Order (Daniel Whitcomb / Maple Hollow Farm)</li>
    </ul>
  </section>

  <section class="column column--right">
    <p class="responsibilities">
      <span class="lead">"CSA Member Responsibilities" - Please Read &#9786;</span>
      As a CSA member, you share in the bounty as well as the potential risks that may occur on the farm. Being a member enables you to form a relationship with the farmer, the farm and the people that are involved with growing the crops. Becoming a member is a commitment. We ask that if you can't finish the season as members, then you are welcome to reassign you share to another family, but we cannot issue refunds.<br>
      If you are unable to pick up your box on delivery day, you must make alternate arrangements for your produce <u>ahead of time</u>. You can have someone else pick up your box, ask the farm not to make your box that week, or ask your site coordinator to hold the box for a later pick-up. If you forget to pick up your share, it will be donated to a food pantry or a neighborhood family. <span class="shout">READ ANY EMAILS THAT WE SEND OUT TO YOU!</span> This is how we communicate with you with announcements, recipes, events and special offers!
    </p>

    <p class="script-heading thanks">“Thank You<br>and Welcome<br>to the Farm!”</p>

    <div class="brand">
      <span class="brand-dot"></span>
      <span class="brand-name">Maple Hollow Farm</span>
    </div>

    <ul class="contact">
      <li>
        <svg viewBox="0 0 32 32" aria-hidden="true"><rect width="32" height="32" rx="4" fill="#1c8a4e"/><rect x="7" y="10" width="18" height="12" fill="none" stroke="#fff" stroke-width="2"/><path d="M7 10l9 7 9-7" fill="none" stroke="#fff" stroke-width="2"/></svg>
        daniel@maplehollowfarm.com
      </li>
      <li>
        <svg viewBox="0 0 32 32" aria-hidden="true"><rect width="32" height="32" rx="4" fill="#1c8a4e"/><path d="M11 7l4 5-2 3c1 3 3 5 6 6l3-2 5 4-2 3c-8 0-17-9-17-17z" fill="#fff"/></svg>
        (555) 014-2283
      </li>
      <li>
        <svg viewBox="0 0 32 32" aria-hidden="true"><rect width="32" height="32" rx="4" fill="#1c8a4e"/><path d="M16 6a7 7 0 0 0-7 7c0 5 7 13 7 13s7-8 7-13a7 7 0 0 0-7-7z" fill="#fff"/><circle cx="16" cy="13" r="2.8" fill="#1c8a4e"/></svg>
        <span>1275 Orchard Lane<br>Fernbrook, Virginia 24099</span>
      </li>
    </ul>
  </section>
</main>
</body>
</html>
```